Rehabilitation Centre Driving Evaluation brochure

I have already designed a brochure when I was at my previous workplace, but need a new one for my own rehab clinic. I will attach the brochure that I already did, as the information hasn't really changed. It is just very old and very ugly. It is an information pamphlet that will be in physician offices. Please let me know if you need anything else.

Target Market(s)

physicians, rehabilitation professionals, therapists, and individuals with medical conditions who want to return to driving

Industry/Entity Type

Medical

Requirements
Nice to have
• I am not stuck on the trifold, and actually may prefer a single fold brochure.

```html
<!DOCTYPE html>
<html lang="en">
<head>
<meta charset="utf-8">
<title>Driving Evaluation and Training Center – Brochure</title>
<link rel="stylesheet" href="https://fonts.googleapis.com/css2?family=Montserrat:wght@400;500;600&family=Oswald:wght@600&display=swap">
<style>
  :root{
    --lime:#b6c40f;
    --navy:#1c4868;
    --navy-deep:#163a56;
    --ink:#4d4d4d;
    --paper:#ffffff;
    --backdrop:#dcdcdc;
    --photo-dark:#3a3a3a;
    --photo-light:#9a9a9a;
  }
  *{margin:0;padding:0;box-sizing:border-box}
  html,body{width:960px;height:1200px;overflow:hidden}
  body{background:var(--backdrop);font-family:"Montserrat",sans-serif;color:var(--ink);position:relative}
  .spread{position:absolute;left:84px;width:792px;height:560px;display:flex;box-shadow:0 10px 30px rgba(0,0,0,.25)}
  .spread--outside{top:40px}
  .spread--inside{top:620px}
  .page{position:relative;width:396px;height:560px;background:var(--paper);overflow:hidden}
  .page + .page{border-left:1px solid #e4e4e4}
  .page svg.shapes{position:absolute;inset:0;width:396px;height:560px}
  .block{position:absolute}
  .section-title{font-weight:400;color:var(--navy);font-size:15px}
  .body-text{font-size:7.5px;line-height:1.4}
  .body-text p + p{margin-top:4px}
  .on-colour{color:#fff}
  .brand{display:flex;align-items:center;gap:6px;font-weight:500;font-size:13px;color:var(--navy)}
  .brand-dot{width:12px;height:12px;border-radius:50%;background:var(--lime)}
  .brand--light{color:#fff}
  .brand--light .brand-dot{background:#fff}
  .contact-list{list-style:none;font-size:9.5px;line-height:1.5;color:#fff}
  .contact-list li{display:flex;align-items:flex-start;gap:8px;margin-bottom:3px}
  .contact-list svg{flex:none;width:10px;height:10px;margin-top:2px}
  .cover-title{font-family:"Oswald",sans-serif;font-weight:600;font-size:27px;line-height:1.05;letter-spacing:-.3px;text-transform:uppercase}
  .cover-title .line-white{color:#fff}
  .cover-title .line-lime{color:var(--lime)}
  .cover-sub{font-size:11px;color:#fff;margin-top:10px;letter-spacing:.2px}
  .web{font-size:8px;color:#9a9a9a}
  .sub-heading{font-weight:600;font-size:10px;color:var(--navy);margin-bottom:2px}
  .service + .service{margin-top:10px}
  .text-heading{font-size:14px;font-weight:400;color:var(--navy);margin-bottom:3px}
  .text-heading--spaced{margin-top:10px}
</style>
</head>
<body>

<section class="spread spread--outside">
  <article class="page page--back">
    <svg class="shapes" viewBox="0 0 396 560" aria-hidden="true">
      <polygon points="0,175 396,95 396,300 0,365" fill="var(--lime)"/>
      <polygon points="0,365 396,300 396,470 0,520" fill="var(--navy)"/>
    </svg>
    <h2 class="block section-title" style="left:34px;top:140px">Referral Process</h2>
    <div class="block body-text on-colour" style="left:34px;top:185px;width:320px">
      <p>Referrals may be made by physicians, therapists, individuals requiring service, insurance companies, case managers, community service agencies, etc. The referral source will be asked to complete a referral form. The client's physician will be contacted and asked to complete a medical referral form stating the client is medically able to participate in the assessment.</p>
      <p>Referrals can be made for any individual who requires an evaluation of their driving skills or adaptive equipment needs by contacting us.</p>
    </div>
    <div class="block brand brand--light" style="left:210px;top:300px"><span class="brand-dot"></span>Northfield Rehabilitation</div>
    <ul class="block contact-list" style="left:34px;top:375px;width:320px">
      <li><svg viewBox="0 0 10 10"><path d="M5 0a3.5 3.5 0 0 0-3.5 3.5C1.5 6 5 10 5 10s3.5-4 3.5-6.5A3.5 3.5 0 0 0 5 0zm0 5a1.4 1.4 0 1 1 0-2.8A1.4 1.4 0 0 1 5 5z" fill="var(--lime)"/></svg><span>482 Maple Crest Road, Unit #4<br>Ridgeton, Ontario, K0L 2B3</span></li>
      <li><svg viewBox="0 0 10 10"><path d="M2 0.5l1.6 2.2-.9 1.1c.6 1.2 1.4 2 2.6 2.6l1.1-.9L8.6 7 8 9.3C4 9 1 6 .7 2z" fill="var(--lime)"/></svg><span>555 014 2287</span></li>
      <li><svg viewBox="0 0 10 10"><rect x="2" y="0.5" width="6" height="3" fill="var(--lime)"/><rect x="0.5" y="4" width="9" height="4" rx="1" fill="var(--lime)"/><rect x="2.5" y="7" width="5" height="2.5" fill="var(--lime)"/></svg><span>555 014 2288</span></li>
      <li><svg viewBox="0 0 10 10"><rect x="0.5" y="2" width="9" height="6.5" fill="none" stroke="var(--lime)"/><path d="M.5 2L5 6l4.5-4" fill="none" stroke="var(--lime)"/></svg><span>office@northfieldrehab.ca</span></li>
      <li><svg viewBox="0 0 10 10"><circle cx="5" cy="5" r="4.3" fill="none" stroke="var(--lime)"/><path d="M.7 5h8.6M5 .7c-2.4 2.5-2.4 6.1 0 8.6M5 .7c2.4 2.5 2.4 6.1 0 8.6" fill="none" stroke="var(--lime)" stroke-width=".8"/></svg><span>www.northfieldrehab.ca</span></li>
    </ul>
  </article>

  <article class="page page--cover">
    <svg class="shapes" viewBox="0 0 396 560" aria-hidden="true">
      <polygon points="40,118 396,95 396,108 40,131" fill="var(--lime)"/>
      <polygon points="0,300 396,262 396,460 0,505" fill="var(--navy)"/>
      <polygon points="0,288 396,250 396,264 0,302" fill="var(--lime)"/>
    </svg>
    <div class="block brand" style="right:30px;top:50px"><span class="brand-dot"></span>Northfield Rehabilitation</div>
    <div class="block" role="img" aria-label="Photograph of a car driving along a misty tree-lined road"
         style="left:40px;top:131px;width:356px;height:165px;background:linear-gradient(160deg,var(--photo-dark),var(--photo-light) 55%,#5a5a5a);clip-path:polygon(0 0,100% 0,100% 72%,0 95%)"></div>
    <div class="block" style="left:26px;top:330px;width:350px">
      <h1 class="cover-title"><span class="line-white">Driving Evaluation</span><br><span class="line-lime">and Training Center</span></h1>
      <p class="cover-sub">A comprehensive driver rehabilitation program</p>
    </div>
    <p class="block web" style="left:40px;top:520px">www.northfieldrehab.ca</p>
  </article>
</section>

<section class="spread spread--inside">
  <article class="page page--inside-left">
    <svg class="shapes" viewBox="0 0 396 560" aria-hidden="true">
      <polygon points="0,110 396,62 396,108 0,156" fill="var(--navy)"/>
      <polygon points="0,156 396,108 396,290 0,330" fill="var(--lime)"/>
      <polygon points="0,552 396,538 396,545 0,560" fill="var(--navy)"/>
    </svg>
    <h2 class="block section-title on-colour" style="left:34px;top:112px;font-size:13px">Reason for Assessment</h2>
    <div class="block" role="img" aria-label="Medical caduceus emblem" style="left:18px;top:180px;width:56px;height:80px;background:var(--navy-deep);opacity:.85;border-radius:4px"></div>
    <div class="block body-text on-colour" style="left:86px;top:158px;width:284px">
      <p>Each physician is required by law to report to the Ministry of Transportation any individual whose driving skills may be affected as a result of illness or injury. Therefore, the client's driver's licence may be placed under medical suspension. If this occurs, the client will be asked to undergo a driving evaluation from a Provincial Driver Assessment Centre.</p>
      <p>Individuals affected by illness, injury, or the aging process, whose driving skills have the potential to be affected, are also encouraged to undergo an evaluation of driving skills. The evaluation is designed to assess each client's ability to safely operate a motor vehicle and provide recommendations as needed.</p>
    </div>
    <div class="block" style="left:30px;top:340px;width:345px">
      <h3 class="text-heading">Eligibility</h3>
      <p class="body-text">Most individuals with disabilities are eligible for an evaluation of their ability to drive. Clients must have a valid driver's licence or the ability to obtain a temporary driver's licence or learner's permit.</p>
      <h3 class="text-heading text-heading--spaced">What we do?</h3>
      <div class="body-text">
        <p>Northfield Rehabilitation is committed to providing optimal rehabilitation service in a cost effective manner.</p>
        <p>We offer a multi-disciplinary, client-centred program of assessment, treatment and consultation for clients with physical, cognitive and/or perceptual impairments. We are aware each client is unique, therefore each program is tailored according to the individual's needs and personal goals.</p>
        <p>The driving assessment and training program is part of our comprehensive rehabilitation services. It is a service which represents our dedication to assist all individuals achieve optimal independence. Driving is an integral skill which is often essential for independence in the community.</p>
      </div>
    </div>
  </article>

  <article class="page page--inside-right">
    <svg class="shapes" viewBox="0 0 396 560" aria-hidden="true">
      <polygon points="120,22 396,0 396,12 120,34" fill="var(--lime)"/>
      <polygon points="0,548 396,520 396,528 0,560" fill="var(--navy)"/>
    </svg>
    <div class="block" role="img" aria-label="Photograph of a hand on a car steering wheel"
         style="left:0;top:34px;width:396px;height:120px;background:linear-gradient(135deg,#cfc4b4,#8a8f96 50%,#2d3640);clip-path:polygon(0 20%,100% 0,100% 80%,0 100%)"></div>
    <h2 class="block section-title" style="left:30px;top:162px">Program Components &amp; Services</h2>
    <div class="block body-text" style="left:30px;top:192px;width:340px">
      <div class="service">
        <h3 class="sub-heading">Clinical Evaluation</h3>
        <p>The client is assessed by a certified occupational therapist. The client is initially seen in clinic for an assessment of physical, cognitive, and perceptual functioning as they relate to driving. The in-clinic portion of the assessment provides the therapist with information regarding medical history, driving history, knowledge of road signs and driving rules, physical abilities, cognitive status, visual and perceptual skills.</p>
      </div>
      <div class="service">
        <h3 class="sub-heading">On the Road Evaluation</h3>
        <p>Following the in-clinic assessment, each client is then assessed in car by the therapist together with a certified driving instructor. The portion of the evaluation provides valuable information regarding the individual's functional driving skills.</p>
      </div>
      <div class="service">
        <h3 class="sub-heading">Evaluation Equipment Needs</h3>
        <p>During the evaluation, it will be determined whether adaptive equipment will be necessary to improve the client's ability to drive safely. Recommendations will be made for adaptive equipment and installation.</p>
      </div>
      <div class="service">
        <h3 class="sub-heading">Training &amp; Follow-up Services</h3>
        <p>Clients are commonly seen following a driving evaluation for training with driving skills or adaptive equipment. Further involvement with the occupational therapist may be indicated for cognitive or perceptual retraining, mobility-aid prescription, vehicle modification, or consultation with appropriate new vehicle purchase.</p>
      </div>
    </div>
  </article>
</section>

</body>
</html>
```